WordPress Website for Pain Relief Clinic

I need a WordPress website designed for my laser pain relief clinic. It needs to be a professional, responsive design with 7 pages: Home, Why Choose Us, Treatable Conditions, Testimonials, FAQ, Franchising, Contact Us. Here is logo: https://files.brivoltcdn.com/media.t-w-e-n.com/sitebuilder/472/CalvexaLogoHighQuality.png

Target Market(s)

people with pain,elderly adults,injuries,soreness

Industry/Entity Type

Clinic

Number of Pages Required

5+ page

Colors
0792cd
85abd2

```html
<!DOCTYPE html>
<html lang="en">
<head>
<meta charset="utf-8">
<title>Calvexa Pain Treatment Center</title>
<link href="https://fonts.googleapis.com/css2?family=Roboto:wght@300;400;500;700&display=swap" rel="stylesheet">
<style>
  :root {
    --brand-blue: #0792cd;
    --soft-blue: #85abd2;
    --text-dark: #222222;
    --text-mid: #444444;
    --white: #ffffff;
    --header-glass: rgba(255, 255, 255, 0.82);
  }
  * { box-sizing: border-box; margin: 0; padding: 0; }
  html, body { width: 1200px; height: 999px; overflow: hidden; background: var(--white); }
  body { font-family: "Roboto", Arial, sans-serif; color: var(--text-dark); position: relative; }

  .hero {
    position: absolute; left: 0; top: 0; width: 1200px; height: 487px;
    background: linear-gradient(90deg, #6b4a36 0%, #8a6a4e 18%, #9fbf6a 30%, #3a3a3a 45%, #cfcac4 60%, #e9e8ea 78%, #c9bdb4 100%);
  }
  .hero-dots { position: absolute; left: 550px; top: 460px; display: flex; gap: 14px; }
  .hero-dot { width: 16px; height: 16px; border-radius: 50%; border: 1.5px solid #2d2d2d; background: rgba(255,255,255,0.15); }
  .hero-dot.is-active { background: var(--soft-blue); border-color: var(--soft-blue); }

  .site-header {
    position: absolute; left: 0; top: 0; width: 1200px; height: 70px; background: var(--header-glass);
  }
  .brand {
    position: absolute; left: 88px; top: 14px; display: flex; align-items: center; gap: 8px;
    font-size: 34px; font-weight: 700; color: var(--brand-blue); line-height: 1;
  }
  .brand-mark { width: 12px; height: 12px; border-radius: 50%; background: var(--brand-blue); }
  .header-phone { position: absolute; right: 77px; top: 6px; font-size: 18px; font-weight: 400; color: var(--soft-blue); }
  .main-nav { position: absolute; top: 36px; left: 0; width: 1200px; height: 34px; font-size: 15px; color: #222; }
  .main-nav a { position: absolute; top: 0; text-decoration: none; color: inherit; white-space: nowrap; }
  .main-nav a.is-current { color: var(--soft-blue); font-weight: 500; }
  .nav-underline { position: absolute; left: 640px; top: 66px; width: 160px; height: 4px; background: var(--soft-blue); }

  .cta-text { position: absolute; left: 170px; top: 515px; font-size: 19px; font-weight: 400; color: var(--text-mid); }
  .cta-button {
    position: absolute; left: 690px; top: 502px; width: 347px; height: 54px; border-radius: 3px;
    background: var(--brand-blue); color: var(--white); font-size: 22px; font-weight: 300;
    display: flex; align-items: center; justify-content: center; text-decoration: none;
  }

  .why-section { position: absolute; left: 0; top: 595px; width: 1200px; text-align: center; }
  .section-title { font-size: 18px; font-weight: 500; color: var(--soft-blue); line-height: 24px; }
  .section-bar { width: 48px; height: 4px; background: var(--soft-blue); margin: 6px auto 0; }
  .section-lead {
    width: 710px; margin: 22px auto 0; font-size: 27px; font-weight: 300; line-height: 30px; color: var(--soft-blue);
  }
  .section-body {
    width: 700px; margin: 21px auto 0; font-size: 16px; font-weight: 400; line-height: 18.8px; color: var(--text-dark);
  }
  .section-body + .section-body { margin-top: 18.8px; }
</style>
</head>
<body>
  <div class="hero" role="img" aria-label="Photo of a patient consulting with a doctor in a white coat at a clinic desk">
    <div class="hero-dots">
      <span class="hero-dot"></span>
      <span class="hero-dot is-active"></span>
      <span class="hero-dot"></span>
      <span class="hero-dot"></span>
    </div>
  </div>

  <header class="site-header">
    <div class="brand"><span>Calvexa</span><span class="brand-mark"></span></div>
    <div class="header-phone">Call 555-014-2273</div>
    <nav class="main-nav">
      <a href="#" style="left:466px">Home</a>
      <a href="#" style="left:528px">Why Choose Us</a>
      <a href="#" class="is-current" style="left:656px">Treatable Conditions</a>
      <a href="#" style="left:811px">Testimonials</a>
      <a href="#" style="left:905px">FAQ</a>
      <a href="#" style="left:964px">Franchising</a>
      <a href="#" style="left:1057px">Contact Us</a>
    </nav>
    <div class="nav-underline"></div>
  </header>

  <p class="cta-text">Say 'No' to pain, consult our doctors now. Or some microcopy.</p>
  <a href="#" class="cta-button">Book An Appointment</a>

  <section class="why-section">
    <h2 class="section-title">Why Choose Us</h2>
    <div class="section-bar"></div>
    <p class="section-lead">Lorem ipsum dolor sit amet, consectetur adipiscing elit. Etiam eget urna a lectus vehicula commodo. Curabitur sit amet libero</p>
    <p class="section-body">Lorem ipsum dolor sit amet, consectetur adipiscing elit. Etiam eget urna a lectus vehicula commodo. Curabitur sit amet libero luctus, lobortis nisl in, scelerisque purus. Etiam sem nisl, imperdiet at sagittis at, placerat a ligula. Duis rhoncus sem non sem porttitor, ut tincidunt quam varius. Morbi a vehicula augue. Donec molestie eu velit a lacinia. Cras accumsan convallis mauris, et gravida ligula accumsan id. Proin tincidunt rutrum neque, mollis vehicula diam lobortis mollis. Vivamus urna neque, efficitur id sem ut, auctor maximus mi. Praesent ultricies faucibus rutrum. Vestibulum ultrices auctor metus. Nulla in volutpat nisl. Aenean tempus, nisi vel tempor euismod, enim mi pellentesque urna, vel hendrerit risus erat nec orci. Integer luctus risus sit amet egestas semper.</p>
    <p class="section-body">Pellentesque auctor pellentesque placerat. Mauris a posuere elit. Nam vehicula ante id lectus ornare molestie. Sed sit amet nibh tempor lectus dictum dapibus ut suscipit odio. Proin dictum et magna nec scelerisque. Mauris ac nulla libero. Etiam eleifend libero purus, sit amet pellentesque nunc mattis in.</p>
  </section>
</body>
</html>
```